Stationery for London Estate Agents (Real Estate)

We are a modern and professional Estate Agency (Realtors) working with high quality properties in London.
We wish to redesign our stationary using our branding displayed on the front of our offices and require a digital version of this logo to be produced (photograph attached). Slight 'tweaking' of this branding is acceptable.
Updates
1st July 2010 Thank you all those designers who have uploaded submissions. Business Card - Details Side: Business Card - Logo Side: Outline of London Skyline Examples of the london skyline are available at http://www.pictovantix.com/searchkwy_london-skyline-silhouette Please be advised that we are looking for an outline, not a 'filled in' silhouette. Letterhead Please feel free to ask us any questions. Bertrand
I have been able to further refine our design requirements based on your submissions.
We like Pale Forks' business card submission that has not been eliminated and have the following design clarifications;
a) Please use an email icon (e.g an envelope).
b) Please make the email as equally prominent as the telephone and fax
c) We very much like VelloTrine's 'mini window icon' - please display the website URL under such a mini window icon at the bottom right of the card.
We are very happy with the colouring, fonts and proportions used by Pale Forks.
We invite designers to try adding an outline of the London Skyline to the left of the large window icon on the business card and in a suitablie position on the Letterhead (e.g at the top left of the letterhead).
We have the following design clarifiications to our Letterhead requirements;
A) We would like the main logo to be on the top right side of the letterhead.
B) We do NOT want the large window icon to be on the left of the logo or the bottom of the letterhead. We are happy having the large window icon to the right or underneath the KB brand.
C) Please use icons for tel, fax and email (e.g. envelope icon for e-mail address)
D) We like two coloured red borders, one at the top and bottom of the letterhead but are happy for variations in shape and size.
E) We currently prefer our address and contact details at the bottom of the letterhead.
F) We like VelloTrine's 'mini window icon' and would prefer this to be used to display the website URL at the bottom right of the letterhead.
G) Please be advised that the letterhead does NOT need additional space for the Company Name as per Pale Forks' submission - the KB brand is sufficient.
Target Market(s)
Owners of high quality property in London.
Industry/Entity Type
Real Estate
Requirements
Must have
- Business Cards: We would like a 'vertical' style business card with our branding on one side and our staff's details on the other;
- Our website is www.korbend.com and we are flexible where that should be on the card and letterhead.
- Stationery details are available in a file attached to this project.
Nice to have
- It would be great to have a horizontal version of the digital logo for placement on property portals (150x60)
Should not have
- Logo should not deviate significantly from the branding on our offices (shop front) - photograph attached.

```html
<!DOCTYPE html>
<html lang="en">
<head>
<meta charset="utf-8">
<title>Korbend Residential – Stationery</title>
<link rel="stylesheet" href="https://fonts.googleapis.com/css2?family=Arimo:wght@400&display=swap">
<style>
  :root {
    --maroon: #8c1f4a;
    --gold: #f6c500;
    --backdrop: #f7c300;
    --paper: #ffffff;
    --ink-light: #ffffff;
  }
  * { margin: 0; padding: 0; box-sizing: border-box; }
  html, body { width: 1200px; height: 905px; overflow: hidden; }
  body {
    background: var(--backdrop);
    font-family: "Arimo", Arial, sans-serif;
    position: relative;
  }

  /* Letterhead */
  .letterhead {
    position: absolute;
    left: 79px; top: 115px;
    width: 466px; height: 659px;
    background: var(--paper);
    box-shadow: 0 2px 8px rgba(0,0,0,0.25);
  }
  .letterhead-band-top { position: absolute; left: 0; top: 0; width: 466px; height: 55px; }
  .letterhead-brand {
    position: absolute; left: 22px; top: 18px;
    color: var(--ink-light); font-size: 15px; letter-spacing: 0.3px;
  }
  .letterhead-address {
    position: absolute; right: 29px; top: 8px;
    color: var(--gold); font-size: 7px;
  }
  .letterhead-tagline {
    position: absolute; left: 212px; top: 37px;
    color: var(--maroon); font-size: 10.5px;
  }
  .letterhead-footer {
    position: absolute; left: 0; bottom: 0;
    width: 466px; height: 46px;
    background: var(--maroon);
  }
  .footer-contacts {
    position: absolute; left: 88px; top: 15px;
    color: var(--gold); font-size: 8px; word-spacing: 1px;
  }
  .footer-web {
    position: absolute; right: 10px; top: 27px;
    color: var(--ink-light); font-size: 9px;
    display: flex; align-items: center; gap: 4px;
  }
  .web-square { width: 8px; height: 8px; background: var(--gold); }

  /* Business cards */
  .card {
    position: absolute; top: 320px;
    width: 90px; height: 201px;
    box-shadow: 0 0 6px rgba(140,31,74,0.55);
    overflow: hidden;
  }
  .card-logo-side { left: 192px; background: var(--maroon); }
  .card-logo-side .card-brand {
    position: absolute; top: 26px; width: 100%; text-align: center;
    color: var(--ink-light); font-size: 10px;
  }
  .card-logo-side .card-tagline {
    position: absolute; top: 67px; width: 100%; text-align: center;
    color: var(--ink-light); font-size: 4.5px;
  }

  .card-details-side { left: 334px; background: var(--paper); }
  .card-head {
    position: absolute; top: 4px; left: 0; width: 100%; height: 32px;
    background: var(--maroon);
  }
  .card-head .card-brand {
    position: absolute; top: 11px; width: 100%; text-align: center;
    color: var(--ink-light); font-size: 8px;
  }
  .card-name {
    position: absolute; top: 66px; width: 100%; text-align: center;
    color: var(--maroon); font-size: 8.5px;
  }
  .card-foot {
    position: absolute; top: 117px; left: 0; width: 100%; height: 84px;
    background: var(--maroon);
    color: var(--gold); font-size: 4.5px; line-height: 1.4;
    padding: 8px 0 0 10px;
  }
  .card-foot p + p { margin-top: 4px; }
  .card-web {
    position: absolute; right: 4px; bottom: 4px;
    color: var(--ink-light); font-size: 4.5px;
    display: flex; flex-direction: column; align-items: flex-end; gap: 2px;
  }
  .card-web .web-square { width: 6px; height: 6px; }
</style>
</head>
<body>

  <section class="letterhead" aria-label="Letterhead">
    <svg class="letterhead-band-top" viewBox="0 0 466 55" aria-hidden="true">
      <path d="M0 0 H466 V29 H209 C185 29 185 55 161 55 H0 Z" fill="var(--maroon)"/>
    </svg>
    <div class="letterhead-brand">Korbend Residential</div>
    <div class="letterhead-address">204 Alder Row, Hampstead, London NW3 9QT</div>
    <div class="letterhead-tagline">Lettings * Sales * Management * Investments</div>

    <footer class="letterhead-footer">
      <div class="footer-contacts">Tel (020 7946 0123) &nbsp; * &nbsp; Fax (020 7946 0188) &nbsp; * &nbsp; Email (info@korbend.com)</div>
      <div class="footer-web"><span class="web-square"></span>www.korbend.com</div>
    </footer>
  </section>

  <section class="card card-logo-side" aria-label="Business card, brand side">
    <div class="card-brand">Korbend Residential</div>
    <div class="card-tagline">Lettings * Sales * Management * Investments</div>
  </section>

  <section class="card card-details-side" aria-label="Business card, details side">
    <div class="card-head"><div class="card-brand">Korbend Residential</div></div>
    <div class="card-name">Bertrand Vale</div>
    <div class="card-foot">
      <p>Address:<br>204 Alder Row,<br>Hampstead, London NW3 9QT</p>
      <p>Tel (020 7946 0123)<br>Fax (020 7946 0188)<br>Mob (07700 900 514)<br>email (bertrand@korbend.com)</p>
    </div>
    <div class="card-web"><span class="web-square"></span>www.korbend.com</div>
  </section>

</body>
</html>
```